Business card

I want a business card the looks like a credit card, must eye-catching !!! I attached some things that I did obviously I want it to LOOK WAY more professional than what I can do....Just some ideas.... that I was thinking

Contact Information for Business Card

Must look like a credit card, I attached some things that I did obviously I want it to LOOK WAY more professional than what I can do....Just some ideas.... that I was thinking

Requirements
Must have
• Must look like a credit card, I attached some things that I did obviously I want it to LOOK WAY more professional than what I can do....Just some ideas.... that I was thinking
Nice to have
Should not have

```html
<!DOCTYPE html>
<html lang="en">
<head>
<meta charset="utf-8">
<title>Kestrel Business Solution — Business Card</title>
<link rel="stylesheet" href="https://fonts.googleapis.com/css2?family=Oswald:wght@600;700&family=Roboto:ital,wght@0,300;0,400;0,700;0,900;1,700&display=swap">
<style>
  :root {
    --page: #e7e7e7;
    --card-deep: #12081c;
    --card-mid: #2a1140;
    --card-glow: #4a1a5e;
    --blue: #1296d8;
    --band-blue: #0e86c0;
    --yellow: #f7c600;
    --white: #ffffff;
    --number-grey: #a3a3a8;
    --label-grey: #9b9ba0;
    --chip-gold: #cfc6a8;
  }
  * { box-sizing: border-box; margin: 0; padding: 0; }
  html, body { width: 1125px; height: 1200px; overflow: hidden; }
  body { background: var(--page); font-family: "Roboto", Arial, sans-serif; position: relative; }

  .card {
    position: absolute;
    left: 151px;
    width: 825px;
    height: 471px;
    border-radius: 22px;
    overflow: hidden;
    background:
      radial-gradient(ellipse at 60% 55%, var(--card-glow) 0%, transparent 55%),
      linear-gradient(135deg, var(--card-deep) 0%, var(--card-mid) 50%, var(--card-deep) 100%);
  }
  .card--front { top: 91px; }
  .card--back { top: 640px; }

  /* Front */
  .chip {
    position: absolute; left: 52px; top: 60px; width: 93px; height: 76px;
    border-radius: 10px;
    background: linear-gradient(135deg, #e6dfc6, var(--chip-gold) 60%, #a9a083);
  }
  .brand { position: absolute; left: 318px; top: 36px; width: 460px; height: 160px; }
  .brand__tag { position: absolute; color: var(--white); font-weight: 700; font-size: 12.5px; letter-spacing: 0.1px; }
  .brand__tag--a { left: 134px; top: 12px; }
  .brand__tag--b { left: 306px; top: 12px; }
  .brand__tag--c { left: 134px; top: 138px; }
  .brand__tag--d { left: 306px; top: 138px; }
  .brand__mark {
    position: absolute; left: 0; top: 38px; width: 92px; height: 92px;
    border-radius: 50%; background: var(--yellow);
  }
  .brand__name {
    position: absolute; left: 108px; top: 36px; width: 360px;
    color: var(--blue); font-weight: 900; line-height: 0.98;
  }
  .brand__name .line1 { display: block; font-size: 62px; letter-spacing: 1px; }
  .brand__name .line2 { display: block; font-size: 28px; }

  .card-number {
    position: absolute; left: 0; right: 0; top: 230px; text-align: center;
    color: var(--number-grey); font-weight: 300; font-size: 44px; letter-spacing: 6px; word-spacing: 22px;
  }
  .holder { position: absolute; left: 50px; top: 318px; }
  .holder__name { font-family: "Oswald", Arial, sans-serif; font-weight: 700; font-size: 48px; color: var(--blue); line-height: 1.1; }
  .holder__phone { font-size: 46px; color: var(--yellow); line-height: 1.05; }
  .valid { position: absolute; left: 432px; top: 366px; color: var(--label-grey); font-size: 20px; line-height: 1.25; }
  .card-type { position: absolute; left: 598px; top: 368px; color: var(--label-grey); font-family: "Oswald", Arial, sans-serif; font-weight: 600; font-size: 28px; font-style: italic; letter-spacing: 0.5px; }

  /* Back */
  .slogan-band {
    position: absolute; left: 0; right: 0; top: 59px; height: 55px;
    background: var(--band-blue); color: var(--white);
    font-size: 29px; text-align: center; line-height: 55px; letter-spacing: 0.3px;
  }
  .slogan-band strong { color: var(--yellow); font-weight: 700; }
  .back-brand {
    position: absolute; left: 36px; top: 300px;
    display: flex; align-items: center; gap: 16px;
  }
  .back-brand__dot { width: 54px; height: 54px; border-radius: 50%; background: var(--yellow); flex: none; }
  .back-brand__name { color: var(--blue); font-weight: 900; font-size: 60px; letter-spacing: 1px; line-height: 1; }
  .contact { position: absolute; left: 415px; top: 180px; width: 340px; text-align: center; }
  .contact__phone { font-family: "Oswald", Arial, sans-serif; font-weight: 700; font-size: 60px; color: var(--blue); line-height: 1; }
  .contact__email { margin-top: 8px; font-size: 13.5px; font-weight: 700; color: var(--yellow); }
  .signature {
    position: absolute; left: 418px; top: 288px; width: 319px; height: 56px;
    background: linear-gradient(180deg, #f4f4f4, #dcdcdc);
    color: #4a4a4a; font-size: 16px; letter-spacing: 1px; text-align: center; line-height: 56px;
  }
  .social { position: absolute; left: 502px; top: 376px; display: flex; gap: 8px; }
  .social__item { width: 44px; height: 44px; border-radius: 7px; background: var(--blue); }
</style>
</head>
<body>
  <section class="card card--front" aria-label="Business card front">
    <div class="chip" role="img" aria-label="Payment card chip"></div>
    <div class="brand">
      <span class="brand__tag brand__tag--a">BUSINESS BROKER</span>
      <span class="brand__tag brand__tag--b">BUSINESS FUNDING</span>
      <span class="brand__mark"></span>
      <div class="brand__name"><span class="line1">KESTREL</span><span class="line2">Business Solution</span></div>
      <span class="brand__tag brand__tag--c">CREDIT CARD PROCESSING</span>
      <span class="brand__tag brand__tag--d">MERCHANT BROKER</span>
    </div>
    <div class="card-number">0720 0104 0122 1208</div>
    <div class="holder">
      <div class="holder__name">DALTON REEVE</div>
      <div class="holder__phone">555-018-2740</div>
    </div>
    <div class="valid">VALID<br>12/50</div>
    <div class="card-type">CREDIT CARD</div>
  </section>

  <section class="card card--back" aria-label="Business card back">
    <div class="slogan-band">EXPERIENCE <strong>BETTER CREDIT CARD</strong> PROCESSING</div>
    <div class="back-brand">
      <span class="back-brand__dot"></span>
      <span class="back-brand__name">KESTREL</span>
    </div>
    <div class="contact">
      <div class="contact__phone">555-018-2740</div>
      <div class="contact__email">KESTRELBIZSOLUTIONS@EXAMPLE.COM</div>
    </div>
    <div class="signature">AUTHORIZED SIGNATURE</div>
    <div class="social" aria-label="Social media links">
      <span class="social__item"></span>
      <span class="social__item"></span>
      <span class="social__item"></span>
    </div>
  </section>
</body>
</html>
```